Business card design needed

I am looking for a simple but elegant business card that has a professional and a classy look and feel about it. Must engage the persons attention.
I own and run multiple dental practices and offer basic to advanced dentistry.

Target Market(s)

people looking for dentists

Industry/Entity Type

Dental

Contact Information for Business Card

Dr. Tobias Hendrikson
K9L Dental
Your Smile My Passion
Rockhampton - 52 Pellinor Street Ph: 0749581624
Emerald - 14 Fenwyck Street Ph: 0749316785
Calliope - Shop 8 27 Tolbarn Drive Ph: 49628437
Email: th@k9ldental.com.au

Requirements
Must have
• Contact Details
QR codes for easy storage and website redirection
email and web address

```html
<!DOCTYPE html>
<html lang="en">
<head>
<meta charset="utf-8">
<title>K9L Dental – Business Card</title>
<link rel="stylesheet" href="https://fonts.googleapis.com/css2?family=Cormorant+Garamond:ital,wght@1,500;1,600&family=Tinos:wght@400&family=Arimo:wght@400&display=swap">
<style>
  :root {
    --page: #ffffff;
    --label: #111111;
    --maroon: #6a0a0c;
    --maroon-deep: #4e0608;
    --gold-light: #f5ecd0;
    --gold-mid: #e2cf9c;
    --gold-deep: #c4a25e;
    --gold-rim: #8a6a24;
    --ink: #141414;
    --accent-red: #8d0f12;
  }
  html, body {
    margin: 0;
    padding: 0;
    width: 1200px;
    height: 496px;
    overflow: hidden;
    background: var(--page);
  }
  .sheet {
    position: relative;
    width: 1250px;
    height: 517px;
    transform: scale(0.96);
    transform-origin: 0 0;
  }
  .side-label {
    position: absolute;
    font-family: "Arimo", Arial, sans-serif;
    font-size: 15px;
    color: var(--label);
    margin: 0;
    transform: translateX(-50%);
  }
  .side-label--front { left: 402px; top: 108px; }
  .side-label--back { left: 877px; top: 123px; }

  .card {
    position: absolute;
    width: 385px;
    height: 221px;
    overflow: hidden;
    box-shadow: 4px 5px 6px rgba(0, 0, 0, 0.35);
  }
  .card--front { left: 223px; top: 158px; }
  .card--back { left: 694px; top: 156px; }
  .card__art {
    position: absolute;
    inset: 0;
    width: 385px;
    height: 221px;
  }

  .card__name {
    position: absolute;
    left: 146px;
    top: 18px;
    margin: 0;
    font-family: "Cormorant Garamond", Georgia, serif;
    font-style: italic;
    font-weight: 600;
    font-size: 24px;
    color: var(--ink);
    white-space: nowrap;
  }
  .card__practice {
    position: absolute;
    left: 195px;
    top: 51px;
    margin: 0;
    font-family: "Cormorant Garamond", Georgia, serif;
    font-style: italic;
    font-weight: 600;
    font-size: 22px;
    color: var(--accent-red);
    white-space: nowrap;
  }
  .contact {
    position: absolute;
    left: 185px;
    top: 105px;
    width: 182px;
    margin: 0;
    font-family: "Tinos", "Times New Roman", serif;
    font-size: 11.5px;
    line-height: 15px;
    color: var(--ink);
    font-style: normal;
  }
  .contact__location {
    display: block;
    white-space: nowrap;
  }
  .contact__location--ruled {
    border-bottom: 1px solid var(--accent-red);
  }
  .contact__line { display: block; white-space: nowrap; }
  .contact__email { color: var(--accent-red); }

  .card__tagline {
    position: absolute;
    left: 162px;
    top: 93px;
    margin: 0;
    font-family: "Cormorant Garamond", Georgia, serif;
    font-style: italic;
    font-weight: 600;
    font-size: 21px;
    color: var(--accent-red);
    white-space: nowrap;
  }
</style>
</head>
<body>
<main class="sheet">
  <p class="side-label side-label--front">Front Side</p>
  <p class="side-label side-label--back">Back Side</p>

  <!-- Front of card -->
  <section class="card card--front" aria-label="Card front">
    <svg class="card__art" viewBox="0 0 385 221" aria-hidden="false">
      <defs>
        <linearGradient id="goldFace" x1="0" y1="0" x2="0" y2="1">
          <stop offset="0" stop-color="var(--gold-deep)"/>
          <stop offset="0.45" stop-color="var(--gold-light)"/>
          <stop offset="1" stop-color="var(--gold-deep)"/>
        </linearGradient>
        <linearGradient id="goldRing" x1="0" y1="0" x2="1" y2="1">
          <stop offset="0" stop-color="#fff4cf"/>
          <stop offset="0.5" stop-color="var(--gold-rim)"/>
          <stop offset="1" stop-color="#f3d98f"/>
        </linearGradient>
        <radialGradient id="goldDisc" cx="0.4" cy="0.35" r="0.75">
          <stop offset="0" stop-color="#fbf2d6"/>
          <stop offset="1" stop-color="var(--gold-deep)"/>
        </radialGradient>
        <radialGradient id="emblemTone" cx="0.45" cy="0.4" r="0.6">
          <stop offset="0" stop-color="#fff6dc"/>
          <stop offset="1" stop-color="#d9bd7c"/>
        </radialGradient>
      </defs>
      <rect class="card__field" width="385" height="221" fill="url(#goldFace)"/>
      <path class="card__band" d="M0 0 H101 C86 70 84 150 76 221 H0 Z" fill="var(--maroon)"/>
      <path class="card__rule" d="M101 0 C86 70 84 150 76 221" fill="none" stroke="var(--gold-rim)" stroke-width="5"/>
      <path class="card__rule" d="M101 0 C86 70 84 150 76 221" fill="none" stroke="#f5dc92" stroke-width="2"/>
      <circle class="emblem__ring" cx="92" cy="109" r="57" fill="url(#goldRing)"/>
      <circle class="emblem__ring-inner" cx="92" cy="109" r="51" fill="var(--gold-rim)"/>
      <circle class="emblem__disc" cx="92" cy="109" r="48" fill="url(#goldDisc)"/>
      <g role="img" aria-label="Gold tooth emblem">
        <ellipse cx="86" cy="103" rx="24" ry="30" fill="url(#emblemTone)"/>
      </g>
    </svg>

    <h1 class="card__name">Dr. Tobias Hendrikson</h1>
    <p class="card__practice">K9L Dental</p>

    <address class="contact">
      <span class="contact__location contact__location--ruled">
        <span class="contact__line">Rockhampton - 52, Pellinor Street</span>
        <span class="contact__line">Ph: 0749581624</span>
      </span>
      <span class="contact__location contact__location--ruled">
        <span class="contact__line">Emerald - 14, Fenwyck Street</span>
        <span class="contact__line">Ph: 0749316785</span>
      </span>
      <span class="contact__location">
        <span class="contact__line">Calliope - Shop 8 27, Tolbarn Drive</span>
        <span class="contact__line">Ph: 49628437</span>
      </span>
      <span class="contact__line contact__email">Email: th@k9ldental.com.au</span>
    </address>
  </section>

  <!-- Back of card -->
  <section class="card card--back" aria-label="Card back">
    <svg class="card__art" viewBox="0 0 385 221">
      <rect class="card__field" width="385" height="221" fill="url(#goldFace)"/>
      <path class="card__band" d="M0 0 H101 C86 70 84 150 76 221 H0 Z" fill="var(--maroon)"/>
      <path class="card__rule" d="M101 0 C86 70 84 150 76 221" fill="none" stroke="var(--gold-rim)" stroke-width="5"/>
      <path class="card__rule" d="M101 0 C86 70 84 150 76 221" fill="none" stroke="#f5dc92" stroke-width="2"/>
      <circle class="emblem__ring" cx="96" cy="110" r="57" fill="url(#goldRing)"/>
      <circle class="emblem__ring-inner" cx="96" cy="110" r="51" fill="var(--gold-rim)"/>
      <circle class="emblem__disc" cx="96" cy="110" r="48" fill="url(#goldDisc)"/>
      <g role="img" aria-label="Gold tooth emblem">
        <ellipse cx="90" cy="104" rx="24" ry="30" fill="url(#emblemTone)"/>
      </g>
    </svg>
    <p class="card__tagline">Your Smile, My Passion..!</p>
  </section>
</main>
</body>
</html>
```